New Web Design Project

Details for my new Web Design Project will be added soon.
Updates
This is my website that need to be work into it www.marlowesquest.com
I am really frustrated with your company, we really need a refund of $556.00 as soon as possible, Do not feel safe to work with.

```html
<!DOCTYPE html>
<html lang="en">
<head>
<meta charset="utf-8">
<title>marlowesquest.com</title>
<link href="https://fonts.googleapis.com/css2?family=Source+Sans+3:wght@400;600;700&display=swap" rel="stylesheet">
<style>
:root{
  --plum:#a84f80;
  --plum-dark:#8a3a68;
  --plum-deep:#6a2a50;
  --page:#f1f1f1;
  --card:#ffffff;
  --ink:#222222;
  --line:#dddddd;
  --footer:#2b2b2b;
  --social:#c8283c;
}
*{box-sizing:border-box;margin:0;padding:0}
html,body{width:830px;height:1200px;overflow:hidden}
body{background:var(--page);font-family:"Source Sans 3",Arial,sans-serif;color:var(--ink);position:relative}
.abs{position:absolute}
.logo{left:155px;top:26px;font-size:20px;color:var(--plum);font-weight:400}
.account{left:497px;top:28px;display:flex;align-items:center;height:24px}
.cart-btn{width:36px;height:24px;display:flex;align-items:center;justify-content:center;border-right:1px solid var(--line)}
.login{font-size:9px;text-decoration:underline;font-weight:600;margin:0 18px 0 17px}
.register{width:92px;height:23px;background:var(--plum);color:#fff;font-size:11px;display:flex;align-items:center;justify-content:space-between;padding:0 12px 0 16px;border-radius:2px}
.nav{left:149px;top:73px;width:538px;height:35px;background:var(--card);display:flex;align-items:center;padding-left:13px;z-index:2}
.nav a{font-size:8.5px;font-weight:600;color:var(--ink);text-decoration:none;padding:0 14px;border-right:1px solid var(--line);line-height:22px}
.nav a:first-child{padding-left:0}
.nav a:last-of-type{border:none}
.search{margin-left:auto;margin-right:22px;width:110px;height:13px;border:1px solid #ccc;border-radius:7px;display:flex;align-items:center;font-size:6px;color:#999;padding-left:8px;position:relative}
.search .go{position:absolute;right:-1px;top:-1px;width:17px;height:13px;background:var(--plum);border-radius:0 7px 7px 0;display:flex;align-items:center;justify-content:center}
.hero{left:0;top:102px;width:830px;height:374px;background:var(--plum)}
.hero-photo{left:512px;top:108px;width:196px;height:334px;background:linear-gradient(180deg,#c9a98c 0%,#f4f2f2 30%,#ffffff 60%,#c2a07e 100%);border-radius:40px 40px 0 0}
.hero-title{left:128px;top:200px;color:#fff;font-weight:700;font-size:26px;line-height:44px;letter-spacing:.2px}
.price-btn{display:flex;align-items:center;height:23px;border-radius:12px;background:var(--plum-dark);color:#fff;overflow:hidden}
.price-btn .price{background:var(--plum-deep);padding:0 8px;height:100%;display:flex;align-items:center;font-size:8px}
.price-btn .get{padding:0 10px;display:flex;align-items:center;gap:8px;font-size:10.5px}
.hero-btn{left:131px;top:357px}
.arrow{width:44px;height:44px;border-radius:50%;background:#fff;display:flex;align-items:center;justify-content:center;top:255px}
.card{background:var(--card);border:1px solid #e4e4e4}
.welcome{left:149px;top:442px;width:538px;height:167px}
.welcome h2{position:absolute;left:33px;top:15px;font-size:13px;color:var(--plum);font-weight:600}
.welcome hr{position:absolute;left:36px;top:39px;width:484px;border:none;border-top:1px solid var(--line)}
.avatar{left:13px;top:52px;width:94px;height:94px;border-radius:50%;border:2px solid #e6e6e6;background:radial-gradient(circle at 50% 40%,#e9c7b4 0%,#d8a6c9 55%,#f3eef2 100%)}
.welcome-copy{left:126px;top:56px;width:390px;font-size:6.3px;line-height:8px}
.welcome-copy p{margin-bottom:9px}
.products{left:149px;top:628px;width:539px;height:464px}
.products h2{position:absolute;left:14px;top:12px;font-size:13px;color:var(--plum);font-weight:600}
.view-all{position:absolute;right:16px;top:18px;font-size:7.5px;font-style:italic;color:#555}
.products hr{position:absolute;left:8px;top:37px;width:522px;border:none;border-top:1px solid var(--line)}
.item{width:127px;height:183px;background:#fff;border:1px solid #e6e6e6}
.item .shot{position:absolute;left:28px;top:5px;width:70px;height:110px}
.item .rule{position:absolute;left:8px;top:121px;width:110px;border-top:1px solid var(--line)}
.item .name{position:absolute;left:4px;right:4px;top:129px;font-size:7px;line-height:11px;text-align:center}
.item .price-btn{position:absolute;left:15px;top:158px;height:15px;width:97px}
.item .price-btn .price{font-size:5.5px;padding:0 8px}
.item .price-btn .get{font-size:7.5px;padding:0 9px;gap:12px}
.col1{left:7px}.col2{left:140px}.col3{left:273px}.col4{left:405px}
.row1{top:58px}.row2{top:249px}
.footer{left:0;top:1133px;width:830px;height:67px;background:var(--footer);color:#fff}
.footer .links{position:absolute;left:150px;top:22px;font-size:7px}
.footer .copy{position:absolute;left:150px;top:38px;font-size:7px}
.socials{position:absolute;left:625px;top:22px;display:flex;gap:5px}
.socials span{width:17px;height:17px;background:var(--social);border-radius:2px}
</style>
</head>
<body>
<div class="abs logo">marlowesquest.com</div>
<div class="abs account">
  <div class="cart-btn"><svg width="10" height="9" viewBox="0 0 10 9"><path d="M0 1h2l1.5 5h5L10 2.5H3" fill="none" stroke="#333" stroke-width="1"/><circle cx="4" cy="8" r=".8" fill="#333"/><circle cx="8" cy="8" r=".8" fill="#333"/></svg></div>
  <span class="login">LOGIN</span>
  <span class="register">REGISTER <svg width="6" height="8" viewBox="0 0 6 8"><path d="M1 1l3 3-3 3" stroke="#fff" stroke-width="1.5" fill="none"/></svg></span>
</div>

<div class="abs hero"></div>
<nav class="abs nav">
  <a href="#">HOME</a><a href="#">PRODUCTS</a><a href="#">ABOUT US</a><a href="#">SEND EMAIL</a><a href="#">CONTACT US</a>
  <div class="search">All Categories<span class="go"><svg width="7" height="7" viewBox="0 0 7 7"><circle cx="3" cy="3" r="2" stroke="#fff" fill="none"/><path d="M4.5 4.5L6.5 6.5" stroke="#fff"/></svg></span></div>
</nav>
<div class="abs hero-photo" role="img" aria-label="White ruffled competition figure skating dress on a mannequin"></div>
<h1 class="abs hero-title">MARLOWE'S QUEST<br>COMPETITION FIGURE SKATING<br>DRESS MQCD01</h1>
<div class="abs price-btn hero-btn"><span class="price">249.99$</span><span class="get">GET NOW <svg width="5" height="8" viewBox="0 0 5 8"><path d="M1 1l3 3-3 3" stroke="#fff" stroke-width="1.4" fill="none"/></svg></span></div>
<div class="abs arrow" style="left:9px"><svg width="14" height="20" viewBox="0 0 14 20"><path d="M11 2L3 10l8 8" stroke="#333" stroke-width="4" fill="none"/></svg></div>
<div class="abs arrow" style="left:773px"><svg width="14" height="20" viewBox="0 0 14 20"><path d="M3 2l8 8-8 8" stroke="#333" stroke-width="4" fill="none"/></svg></div>

<section class="abs card welcome">
  <h2>Welcome to Marlowesquest.com</h2>
  <hr>
  <div class="abs avatar" role="img" aria-label="Young skater in a pink velvet dress"></div>
  <div class="abs welcome-copy">
    <p>Marlowe's Quest specializes in designing and creating high-end designed competition figure skating dresses and costumes for figure skaters including baton twirling, majorettes, drill team uniforms, or dancer costumes in United States.</p>
    <p>We are local maufacturer of quality skate and sportswear and are based in the United States.</p>
    <p>We are proudly manufacture all our products here, however, we specialize both in domestic as well as international orders.</p>
    <p>For wholesale please contact us either by phone or email for more information.</p>
    <p>Like US @ social.example.com/marlowesquest</p>
  </div>
</section>

<section class="abs card products">
  <h2>Our Products</h2>
  <span class="view-all">&#9656; view all products</span>
  <hr>
  <div class="abs item col1 row1"><div class="shot" role="img" aria-label="Black yoga pants with flame print" style="background:linear-gradient(180deg,#2a1a14,#d8641c 50%,#1e1414)"></div><div class="rule"></div><div class="name">FIRE FLAMMY YOGA PANT<br>MQYP01</div><div class="price-btn"><span class="price">49.99$</span><span class="get">GET NOW &rsaquo;</span></div></div>
  <div class="abs item col2 row1"><div class="shot" role="img" aria-label="Black fold-over boot cut yoga pants" style="background:linear-gradient(180deg,#2a2a2a,#0d0d0d)"></div><div class="rule"></div><div class="name">YOGA PANT FOLD OVER BOOT<br>CUT MQYP07</div><div class="price-btn"><span class="price">44.99$</span><span class="get">GET NOW &rsaquo;</span></div></div>
  <div class="abs item col3 row1"><div class="shot" role="img" aria-label="Black skirted capri yoga pants" style="background:linear-gradient(180deg,#222,#3a3a3a 70%,#c7a488)"></div><div class="rule"></div><div class="name">SKIRTPANTS YOGA CAPRI ALL<br>BLACK MQYP03</div><div class="price-btn"><span class="price">49.99$</span><span class="get">GET NOW &rsaquo;</span></div></div>
  <div class="abs item col4 row1"><div class="shot" role="img" aria-label="Black long-sleeve skating shirt with turquoise accent" style="background:linear-gradient(180deg,#4cc6c0 0%,#1b1b1b 25%,#111)"></div><div class="rule"></div><div class="name">SHIRT WITH SIDE BOW FIGURE<br>SKATING PANTS TURQUOISE SP02</div><div class="price-btn"><span class="price">98.99$</span><span class="get">GET NOW &rsaquo;</span></div></div>

  <div class="abs item col1 row2"><div class="shot" role="img" aria-label="Black boyshorts with blue lips print" style="background:linear-gradient(180deg,#1e5f8a,#0f2a40 60%,#c9a385)"></div><div class="rule"></div><div class="name">SEXY LIPPY BOYSHORTS<br>MQSHORT01</div><div class="price-btn"><span class="price">28.99$</span><span class="get">GET NOW &rsaquo;</span></div></div>
  <div class="abs item col2 row2"><div class="shot" role="img" aria-label="Dark green velvet competition skating dress" style="background:linear-gradient(180deg,#e3c8b6,#1f5a4c 40%,#163f36)"></div><div class="rule"></div><div class="name">MARLOWE'S QUEST BEAUTIFUL<br>COMPETITION SKATING DRESS</div><div class="price-btn"><span class="price">269.99$</span><span class="get">GET NOW &rsaquo;</span></div></div>
  <div class="abs item col3 row2"><div class="shot" role="img" aria-label="Black skating skirt with red cherry print" style="background:linear-gradient(180deg,#c89e86,#2a1416 35%,#8e1e28)"></div><div class="rule"></div><div class="name">MQ SKIRT MQS01 RED CHERRY ICE<br>FIGURE SKATING</div><div class="price-btn"><span class="price">59.99$</span><span class="get">GET NOW &rsaquo;</span></div></div>
  <div class="abs item col4 row2"><div class="shot" role="img" aria-label="Purple and black gymnastic leotard on a mannequin" style="background:linear-gradient(180deg,#6a3ea0,#1c1c2e 50%,#2d2a3a)"></div><div class="rule"></div><div class="name">MARLOWE'S QUEST<br>GYMNASTIC LEOTARD MQG01</div><div class="price-btn"><span class="price">64.99$</span><span class="get">GET NOW &rsaquo;</span></div></div>
</section>

<footer class="abs footer">
  <div class="links">Home &nbsp;|&nbsp; About Us &nbsp;|&nbsp; Privacy Policy &nbsp;|&nbsp; Send Email &nbsp;|&nbsp; Site Map &nbsp;|&nbsp; View Cart</div>
  <div class="copy">Copyright 2014 Marlowe's Quest Inc. &nbsp;|&nbsp; All rights reserved</div>
  <div class="socials" aria-label="Social links"><span></span><span></span><span></span></div>
</footer>
</body>
</html>
```